New Banner Ad Design Project

We are a start-up in San Francisco that sells consignment clothes with a percentage of the proceeds donated to charity. Also, volunteer groups can conduct dress drives and send them to us and we will sell them and give their charity back 60% of the proceeds.

We have several uses for banners:
- Home page banner:
- Promote timely Flash Sales (they last only 96 hours) which happen 2x/week
- Promote how good it feels to give back and shop
- Promote any special promotions such as a Gift With Purchase
- Community banner:
- Promote the lifestyle
- Promote any particular group conducting a dress drive

If you are going to submit one banner it is to be for an upcoming sale, as the two attached files address (maternity sale). If we find the right designer we will consider working with them beyond the design contest for future sale banners as well as others

We consider our 'competitors' to be The Garment Quarter, The TrueLoop, KlosetSwap, KlosetHop, WornAgain. Our key differentiator is the charitable components and how groups are conducting dress drives to raise money.

We are in the midst of changing our company name, tagline and logo. The new company will be called 'TelaLume' and our tagline is 'Rewoven Kindness'

Target Market(s)

Our initial audience is young women 16 - 30. We will be focusing on Prom February through May which appeals to 16 - 18 year olds.

We also have maternity-wear. We want these women to feel fashionable

We are focused on individuals who want to give back.

Industry/Entity Type

Charity

Font styles to use
Serif
Sans Serif

Colors
8769ae
1b1b1b
474747
c3c3c3
86cfc6
b7a5cd

Requirements
Must have
• - Youthful and stylish voice (not to be confused with Young)
- Appealing visuals
- Powerful call-to-action as it pertains to banners for our flash sales
- An inclusive feel
- Communicates our charitable component
Nice to have
• - Emotional appeal
- Women wearing our clothes (see attached)
Should not have
• - Too much text
- Too girly; overly flowery

```html
<!DOCTYPE html>
<html lang="en">
<head>
<meta charset="utf-8">
<title>Maternity Sale Banner</title>
<link rel="stylesheet" href="https://fonts.googleapis.com/css2?family=Raleway:wght@200;300;800&display=swap">
<style>
  :root {
    --banner-grey: #999898;
    --type-white: #ffffff;
    --cta-purple: #5c3d72;
    --photo-cream: #f6f1e6;
    --photo-skin: #e6b59a;
    --photo-dark: #2d2a28;
  }
  html, body {
    margin: 0;
    padding: 0;
    width: 1200px;
    height: 553px;
    overflow: hidden;
    background: var(--banner-grey);
  }
  .sale-banner {
    display: block;
    width: 1200px;
    height: 553px;
    font-family: "Raleway", "Helvetica Neue", Arial, sans-serif;
  }
  .banner-bg { fill: var(--banner-grey); }
  .headline-category {
    fill: var(--type-white);
    font-weight: 200;
    font-size: 136px;
  }
  .headline-sale {
    font-weight: 800;
    font-size: 318px;
  }
  .charity-note {
    fill: var(--type-white);
    font-weight: 300;
    font-size: 36px;
  }
  .cta-circle { fill: var(--cta-purple); }
  .cta-label {
    fill: var(--type-white);
    font-weight: 300;
    font-size: 42px;
  }
  .cta-bag { fill: var(--type-white); }
  .cta-bag-handle {
    fill: none;
    stroke: var(--type-white);
    stroke-width: 2.5;
  }
</style>
</head>
<body>
<svg class="sale-banner" viewBox="0 0 1200 553" xmlns="http://www.w3.org/2000/svg">
  <defs>
    <linearGradient id="sale-photo-fill" x1="0" y1="0" x2="1" y2="0">
      <stop offset="0" stop-color="var(--photo-cream)"/>
      <stop offset="0.28" stop-color="var(--photo-skin)"/>
      <stop offset="0.5" stop-color="var(--photo-skin)"/>
      <stop offset="0.62" stop-color="var(--photo-dark)" stop-opacity="0.55"/>
      <stop offset="0.78" stop-color="var(--photo-cream)"/>
      <stop offset="1" stop-color="var(--photo-cream)"/>
    </linearGradient>
  </defs>

  <rect class="banner-bg" x="0" y="0" width="1200" height="553"/>

  <text class="headline-category" x="83" y="171" textLength="783" lengthAdjust="spacingAndGlyphs">MATERNITY</text>

  <g role="img" aria-label="Fashion photo of a woman in sunglasses with red lipstick, seen through the letters of SALE">
    <text class="headline-sale" x="80" y="415" textLength="776" lengthAdjust="spacingAndGlyphs" fill="url(#sale-photo-fill)">SALE</text>
  </g>

  <text class="charity-note" x="77" y="463" textLength="777" lengthAdjust="spacingAndGlyphs">60% OF YOUR PURCHASE GOES TO CHARITY</text>

  <g class="cta-shop-now">
    <circle class="cta-circle" cx="1032" cy="284" r="134"/>
    <text class="cta-label" x="1032" y="279" text-anchor="middle" textLength="210" lengthAdjust="spacingAndGlyphs">SHOP NOW</text>
    <path class="cta-bag-handle" d="M1022 305 v-10 a11 11 0 0 1 22 0 v10"/>
    <path class="cta-bag" d="M1012 300 L1054 298 L1062 360 L1005 362 Z"/>
  </g>
</svg>
</body>
</html>
```